plumbing & gas fitting business card design

We need a business card design for a plumbing & gas fitting company. The company covers commercial, domestic and maintenance work. We would like a modern design communicating efficiency and sophistication. preferred colours would include (red grey & black) or (green grey & black). Please DO NOT include any water droplets.

Industry/Entity Type

Business

Contact Information for Business Card

Vortig Plumbing & Gas, Commercial Domestic & Maintenance, licence no. 617394K, ABN 47215830962, Phone 0417382956, Email vortigplumbingandgas@corvanet.com

```html
<!DOCTYPE html>
<html lang="en">
<head>
<meta charset="utf-8">
<title>Vortig Plumbing &amp; Gas – Business Card</title>
<link rel="stylesheet" href="https://fonts.googleapis.com/css2?family=Arimo:wght@400&display=swap">
<style>
  :root {
    --red-187: #c8002c;
    --black: #000000;
    --grey-423: #8e8e8e;
    --grey-406: #d5cbcb;
    --paper: #ffffff;
  }
  html, body {
    margin: 0;
    padding: 0;
    width: 1200px;
    height: 1000px;
    overflow: hidden;
    background: var(--paper);
  }
  .canvas {
    display: block;
    width: 1200px;
    height: 1000px;
    font-family: "Arimo", Helvetica, Arial, sans-serif;
  }
  .card-frame { fill: var(--red-187); }
  .card-field { fill: var(--black); }
  .accent-bar { fill: var(--red-187); }
  .company-name { fill: var(--grey-406); font-size: 44px; }
  .detail { font-size: 41px; }
  .detail-label { fill: var(--grey-423); }
  .detail-value { fill: var(--grey-406); }
  .email-label { fill: var(--grey-423); font-size: 42px; }
  .email-address { fill: var(--grey-406); font-size: 42px; }
  .swatch-red { fill: var(--red-187); }
  .swatch-black { fill: var(--black); }
  .swatch-grey { fill: var(--grey-423); }
  .swatch-light { fill: var(--grey-406); }
  .swatch-label { fill: var(--black); font-size: 33px; text-anchor: middle; }
</style>
</head>
<body>
<svg class="canvas" viewBox="0 0 1200 1000" xmlns="http://www.w3.org/2000/svg">
  <g class="business-card">
    <rect class="card-frame" x="78" y="52" width="1063" height="615"/>
    <rect class="card-field" x="89" y="63" width="1041" height="593"/>
    <rect class="accent-bar accent-bar--vertical" x="119" y="92" width="94" height="564"/>
    <rect class="accent-bar accent-bar--upper" x="407" y="233" width="723" height="24"/>
    <rect class="accent-bar accent-bar--lower" x="213" y="463" width="684" height="26"/>

    <text class="company-name" x="218" y="143">Vortig Plumbing &amp; Gas, Commercial</text>
    <text class="company-name" x="218" y="203">Domestic &amp; Maintenance</text>

    <text class="detail" x="637" y="314"><tspan class="detail-label">Licence no. </tspan><tspan class="detail-value">617394K</tspan></text>
    <text class="detail" x="641" y="375"><tspan class="detail-label">ABN </tspan><tspan class="detail-value">47215830962</tspan></text>
    <text class="detail" x="638" y="437"><tspan class="detail-label">Phone </tspan><tspan class="detail-value">0417382956</tspan></text>

    <text class="email-label" x="225" y="555">Email</text>
    <text class="email-address" x="225" y="623">vortigplumbingandgas@corvanet.com</text>
  </g>

  <g class="colour-palette">
    <rect class="swatch-red" x="80" y="723" width="143" height="144"/>
    <rect class="swatch-black" x="246" y="723" width="144" height="144"/>
    <rect class="swatch-grey" x="413" y="723" width="144" height="144"/>
    <rect class="swatch-light" x="580" y="723" width="144" height="144"/>

    <text class="swatch-label" x="153" y="896">Chromex</text>
    <text class="swatch-label" x="151" y="933">187M</text>
    <text class="swatch-label" x="319" y="905">BLACK</text>
    <text class="swatch-label" x="486" y="896">Chromex</text>
    <text class="swatch-label" x="484" y="933">423M</text>
    <text class="swatch-label" x="653" y="896">Chromex</text>
    <text class="swatch-label" x="651" y="933">406M</text>
  </g>
</svg>
</body>
</html>
```